I need a label design for my up coming wine bottle

The bottle is a standard wine bottle, 720 ML. The label needs to be elegant 1-3 colors preferably with grape vines highlighting my winery name. 5-8 cellars

```html
<!DOCTYPE html>
<html lang="en">
<head>
<meta charset="utf-8">
<title>5-8 Cellars Wine Label</title>
<link rel="stylesheet" href="https://fonts.googleapis.com/css2?family=Cinzel:wght@400;500;600&display=swap">
<style>
  :root {
    --backdrop: #dcdcdc;
    --paper: #f3f2ef;
    --paper-shade: #e6e5e1;
    --wine-red: #b00f31;
    --ink: #1c1c1c;
    --band-text: #f7eef0;
  }
  * { margin: 0; padding: 0; box-sizing: border-box; }
  html, body {
    width: 1200px;
    height: 1040px;
    overflow: hidden;
    background: var(--backdrop);
  }
  .label {
    position: absolute;
    left: 187px;
    top: 30px;
    width: 826px;
    height: 980px;
    background: radial-gradient(ellipse at 50% 40%, var(--paper) 55%, var(--paper-shade) 100%);
    clip-path: polygon(0% 4%, 5% 3.2%, 9% 4.4%, 14% 3.4%, 20% 4.2%, 26% 3%, 31% 3.8%, 37% 2.6%, 43% 3.6%, 49% 2.8%, 55% 3.5%, 61% 2.4%, 67% 3.2%, 73% 2.2%, 79% 3%, 85% 2.4%, 91% 3.2%, 96% 2.6%, 100% 3.4%, 100% 100%, 0% 100%);
  }
  .vine-illustration {
    position: absolute;
    left: 155px;
    top: 98px;
    width: 512px;
    height: 524px;
    background: radial-gradient(ellipse at 50% 55%, #8f8f8f 0%, #c9c9c7 55%, var(--paper) 100%);
    border-radius: 48%;
  }
  .tagline, .winery-name, .subline, .band-text {
    font-family: "Cinzel", serif;
    text-transform: uppercase;
    text-align: center;
  }
  .tagline {
    position: absolute;
    top: 682px;
    left: 0;
    width: 100%;
    font-size: 16px;
    letter-spacing: 8px;
    color: var(--ink);
  }
  .winery-name {
    position: absolute;
    top: 722px;
    left: 0;
    width: 100%;
    font-size: 80px;
    font-weight: 600;
    line-height: 1.2;
    letter-spacing: 2px;
    color: var(--ink);
  }
  .subline {
    position: absolute;
    top: 836px;
    left: 0;
    width: 100%;
    font-size: 20px;
    letter-spacing: 13px;
    color: var(--ink);
  }
  .info-band {
    position: absolute;
    left: 0;
    bottom: 0;
    width: 100%;
    height: 79px;
    background: var(--wine-red);
    display: flex;
    align-items: center;
    justify-content: space-between;
    padding: 0 60px;
  }
  .band-text {
    color: var(--band-text);
    font-size: 19px;
    font-weight: 500;
  }
</style>
</head>
<body>
  <main class="label">
    <div class="vine-illustration" role="img" aria-label="Engraved ink drawing of a grape cluster hanging from a vine with leaves"></div>
    <p class="tagline">Premium Quality</p>
    <h1 class="winery-name">5-8 Cellars</h1>
    <p class="subline">Lorem Ipsum Dolor</p>
    <footer class="info-band">
      <span class="band-text">750 ml</span>
      <span class="band-text">Wine of Country Name</span>
      <span class="band-text">14%ABV</span>
    </footer>
  </main>
</body>
</html>
```